KALVERIA Consultancy Business Card

We need a business card design for a new Image & Etiquette Consultancy Company.

The design should reflect the corporate colour found in the logo attached.

Info to include:

Name: Melba Tran
Title: Image Consultant
Company: KAL VERIA CONSULTANCY
Address: 27 Kelso Street, #14-09 Harbourline Tower, Singapore 058217
Contact: 9317 6284
Email: melba@kalveria.com.sg
Website: www.kalveria.com.sg

```html
<!DOCTYPE html>
<html lang="en">
<head>
<meta charset="utf-8">
<title>Kal Veria Consultancy – Business Card</title>
<link href="https://fonts.googleapis.com/css2?family=Open+Sans:wght@400;600;700&display=swap" rel="stylesheet">
<style>
  :root {
    --backdrop: #ece8e3;
    --card-black: #050505;
    --card-white: #ffffff;
    --gold: #d9a91c;
    --gold-deep: #c48f27;
    --gold-light: #ecc42a;
    --silver: #d8d8d8;
    --plum: #3a1f4d;
    --ink-light: #ffffff;
  }
  html, body {
    margin: 0;
    padding: 0;
    width: 1200px;
    height: 1081px;
    overflow: hidden;
    background: var(--backdrop);
    font-family: "Open Sans", Arial, sans-serif;
  }
  .canvas {
    position: relative;
    width: 1200px;
    height: 1081px;
  }
  .card {
    position: absolute;
    width: 822px;
    height: 470px;
    border-radius: 40px;
    overflow: hidden;
    box-shadow: 0 6px 18px rgba(0,0,0,0.18);
  }
  .card-back { left: 332px; top: 41px; background: var(--card-black); }
  .card-front { left: 44px; top: 553px; background: var(--card-white); }
  .card-art { position: absolute; inset: 0; }
  .brand-name {
    position: absolute;
    left: 0; right: 0;
    text-align: center;
    font-weight: 600;
    font-size: 64px;
    letter-spacing: 4px;
    line-height: 1;
    margin: 0;
  }
  .card-back .brand-name { top: 80px; color: var(--gold); }
  .card-front .brand-name { top: 165px; color: var(--plum); }
  .contact {
    position: absolute;
    left: 0; right: 0;
    top: 222px;
    text-align: center;
    color: var(--ink-light);
    font-size: 18px;
    line-height: 1.55;
  }
  .contact-row {
    display: flex;
    justify-content: center;
    align-items: center;
    gap: 8px;
  }
  .contact-row svg { width: 17px; height: 17px; flex: none; }
  .contact-gap { margin-left: 10px; }
  .address { margin-top: 20px; line-height: 1.45; }
  .person {
    position: absolute;
    left: 0; right: 0;
    top: 430px;
    margin: 0;
    text-align: center;
    color: var(--ink-light);
    font-size: 21px;
    line-height: 26px;
  }
  .person-name { font-weight: 700; }
  .website {
    position: absolute;
    left: 0; right: 0;
    top: 372px;
    margin: 0;
    text-align: center;
    color: var(--plum);
    font-size: 22px;
    line-height: 30px;
    letter-spacing: 2px;
  }
  .website strong { font-weight: 700; }
</style>
</head>
<body>
<main class="canvas">

  <section class="card card-back">
    <svg class="card-art" viewBox="0 0 822 470" aria-hidden="true">
      <defs>
        <linearGradient id="goldBand" x1="0" y1="0" x2="1" y2="0">
          <stop offset="0" stop-color="#ecc42a"/>
          <stop offset="0.6" stop-color="#d9a91c"/>
          <stop offset="1" stop-color="#c48f27"/>
        </linearGradient>
        <linearGradient id="silverSweep" x1="0" y1="0" x2="1" y2="0">
          <stop offset="0" stop-color="#9a9a9a"/>
          <stop offset="0.35" stop-color="#ffffff"/>
          <stop offset="0.7" stop-color="#d8d8d8"/>
          <stop offset="1" stop-color="#8c8c8c"/>
        </linearGradient>
      </defs>
      <path class="gold-band" d="M0,334 C260,380 560,400 822,388 L822,470 L0,470 Z" fill="url(#goldBand)"/>
      <path class="silver-sweep" d="M0,298 C220,362 520,394 822,388 L822,394 C520,404 230,388 0,336 Z" fill="url(#silverSweep)"/>
    </svg>

    <h1 class="brand-name">KALVERIA</h1>

    <div class="contact">
      <div class="contact-row">
        <svg viewBox="0 0 16 16" aria-hidden="true"><circle cx="8" cy="8" r="8" fill="#fff"/><path d="M5.2 3.8l1.6 1.6-.9 1.1c.6 1.3 1.5 2.2 2.8 2.8l1.1-.9 1.6 1.6-1 1.4c-3 -.4-5.6-3-6-6z" fill="#000"/></svg>
        <span>9317 6284</span>
      </div>
      <div class="contact-row">
        <svg viewBox="0 0 16 16" aria-hidden="true"><circle cx="8" cy="8" r="8" fill="#fff"/><rect x="3.5" y="5" width="9" height="6" fill="#000"/><path d="M3.5 5l4.5 3.5 4.5-3.5" stroke="#fff" stroke-width="1" fill="none"/></svg>
        <span>melba@kalveria.com.sg</span>
        <svg class="contact-gap" viewBox="0 0 16 16" aria-hidden="true"><circle cx="8" cy="8" r="8" fill="#fff"/><circle cx="8" cy="8" r="5" fill="none" stroke="#000" stroke-width="1.2"/><ellipse cx="8" cy="8" rx="2.2" ry="5" fill="none" stroke="#000" stroke-width="1"/><path d="M3 8h10" stroke="#000" stroke-width="1"/></svg>
        <span>www.kalveria.com.sg</span>
      </div>
      <div class="address">
        27 Kelso Street, #14-09 Harbourline Tower<br>
        Singapore 058217
      </div>
    </div>

    <p class="person"><span class="person-name">Melba Tran ,</span> Image Consultant</p>
  </section>

  <section class="card card-front">
    <h2 class="brand-name">KALVERIA</h2>
    <p class="website">www.<strong>kalveria</strong>.com.sg</p>
  </section>

</main>
</body>
</html>
```